Business card for auto dealership

Looking for a clean modern design.
Would like attached logo incorporated

Industry/Entity Type

Car dealership

Contact Information for Business Card

Name, website, phone, cell, fax, email

```html
<!DOCTYPE html>
<html lang="en">
<head>
<meta charset="utf-8">
<title>Halvorsen Truck &amp; Auto Sales – Business Card</title>
<link href="https://fonts.googleapis.com/css2?family=Oswald:wght@600&family=Source+Sans+3:wght@400;600;700&display=swap" rel="stylesheet">
<style>
  :root {
    --backdrop: #e4e4e4;
    --card: #2b2a2a;
    --ink: #ffffff;
    --ink-soft: #e8e8e8;
    --mark-dark: #121212;
  }
  * { margin: 0; padding: 0; box-sizing: border-box; }
  html, body { width: 1200px; height: 960px; overflow: hidden; }
  body {
    position: relative;
    background: var(--backdrop);
    font-family: "Source Sans 3", sans-serif;
    color: var(--ink);
  }
  .card {
    position: absolute;
    left: 296px;
    width: 612px;
    height: 350px;
    background: var(--card);
    overflow: hidden;
  }
  .card--front { top: 103px; }
  .card--back { top: 507px; }

  /* Front wordmark */
  .wordmark {
    position: absolute;
    left: 0; right: 0;
    top: 112px;
    text-align: center;
    font-weight: 600;
    color: var(--ink);
    line-height: 1;
  }
  .wordmark__name { font-size: 78px; letter-spacing: 1px; }
  .wordmark__tagline { font-size: 17px; font-weight: 700; letter-spacing: 1px; margin-top: 6px; text-transform: uppercase; }

  /* Back vertical wordmark: laid out horizontally, turned a quarter clockwise */
  .wordmark-vertical {
    position: absolute;
    left: 46px;
    top: 50px;
    width: 258px;
    white-space: nowrap;
    color: var(--mark-dark);
    line-height: 1;
    transform-origin: top left;
    transform: translateX(68px) rotate(90deg);
  }
  .wordmark-vertical__name {
    display: block;
    font-size: 52px;
    font-weight: 600;
    letter-spacing: 1px;
  }
  .wordmark-vertical__tagline {
    display: block;
    font-size: 13px;
    font-weight: 700;
    letter-spacing: 0.5px;
    text-transform: uppercase;
    margin-top: 3px;
  }

  /* Contact block */
  .contact {
    position: absolute;
    left: 356px;
    top: 78px;
  }
  .contact__name {
    font-family: "Oswald", sans-serif;
    font-weight: 600;
    font-size: 25px;
    line-height: 1.1;
    color: var(--ink);
  }
  .contact__role {
    font-size: 15px;
    margin-top: 3px;
    color: var(--ink-soft);
  }
  .contact__rule {
    width: 34px;
    height: 2px;
    background: var(--ink);
    margin-top: 32px;
  }
  .contact__list {
    list-style: none;
    margin-top: 39px;
  }
  .contact__item {
    display: flex;
    align-items: center;
    height: 20.5px;
    font-size: 14.5px;
    color: var(--ink-soft);
  }
  .contact__icon {
    width: 13px;
    height: 13px;
    margin-right: 8px;
    flex: none;
  }
</style>
</head>
<body>

<section class="card card--front" aria-label="Card front">
  <div class="wordmark">
    <div class="wordmark__name">Halvorsen</div>
    <div class="wordmark__tagline">Truck &amp; Auto Sales</div>
  </div>
</section>

<section class="card card--back" aria-label="Card back">
  <div class="wordmark-vertical" aria-hidden="true">
    <span class="wordmark-vertical__name">Halvorsen</span>
    <span class="wordmark-vertical__tagline">Truck &amp; Auto Sales</span>
  </div>

  <div class="contact">
    <h1 class="contact__name">Dana Halvorsen</h1>
    <p class="contact__role">Founder &amp; Owner</p>
    <div class="contact__rule"></div>
    <ul class="contact__list">
      <li class="contact__item">
        <svg class="contact__icon" viewBox="0 0 16 16" fill="none" stroke="#fff" stroke-width="1.6"><path d="M3 2h3l1.5 3.5-2 1.2a8 8 0 0 0 3.8 3.8l1.2-2L14 10v3a1 1 0 0 1-1 1A11 11 0 0 1 2 3a1 1 0 0 1 1-1z"/></svg>
        585-555-0142
      </li>
      <li class="contact__item">
        <svg class="contact__icon" viewBox="0 0 16 16" fill="none" stroke="#fff" stroke-width="1.6"><rect x="4" y="1" width="8" height="14" rx="1.5"/><line x1="7" y1="12.5" x2="9" y2="12.5"/></svg>
        585-555-0187
      </li>
      <li class="contact__item">
        <svg class="contact__icon" viewBox="0 0 16 16" fill="#fff"><rect x="4" y="1" width="8" height="4"/><rect x="1" y="6" width="14" height="6" rx="1"/><rect x="4" y="11" width="8" height="4"/></svg>
        585-555-0119
      </li>
      <li class="contact__item">
        <svg class="contact__icon" viewBox="0 0 16 16" fill="none" stroke="#fff" stroke-width="1.6"><rect x="1" y="3" width="14" height="10"/><path d="M1 3l7 6 7-6"/></svg>
        dana@halvorsenauto.com
      </li>
      <li class="contact__item">
        <svg class="contact__icon" viewBox="0 0 16 16" fill="none" stroke="#fff" stroke-width="1.3"><circle cx="8" cy="8" r="6.5"/><ellipse cx="8" cy="8" rx="3" ry="6.5"/><line x1="1.5" y1="8" x2="14.5" y2="8"/></svg>
        www.Halvorsenauto.com
      </li>
    </ul>
  </div>
</section>

</body>
</html>
```